Business Card Design

Selling Televisions, Velmora, Kira, Dravelux, Ronavi
The latest models, sizes ranging from 22"- 75"
Surround Sounds, Sound Bars and Wall Mounts

Target Market(s)

Mainly males/boys/blokes etc

Industry/Entity Type

Business

Contact Information for Business Card

Glen Marsh
07841526094
glmarsh@quinvale-mail.com

Requirements
Must have
• simplistic design, probably just 2 of the images used

clarity essential
Nice to have
• Metallic if possible

```html
<!DOCTYPE html>
<html lang="en">
<head>
<meta charset="utf-8">
<title>Glen Marsh – Business Card</title>
<link rel="stylesheet" href="https://fonts.googleapis.com/css2?family=Syncopate:wght@700&family=Oswald:wght@400&family=Archivo+Narrow:wght@400&display=swap">
<style>
  :root {
    --page-bg: #3b3735;
    --card-white: #ffffff;
    --slate-dark: #2c3d49;
    --slate-mid: #435a69;
    --slate-band: #8ea5b4;
    --ink: #1f1f1f;
    --icon-blue: #2d5a86;
    --text-light: #f2f5f7;
    --screen-dark: #1c2533;
    --screen-mid: #6d6f8c;
  }
  html, body {
    margin: 0;
    padding: 0;
    width: 1200px;
    height: 840px;
    overflow: hidden;
    background: var(--page-bg);
  }
  .business-card {
    position: absolute;
    left: 60px;
    top: 63px;
    width: 1080px;
    height: 714px;
    overflow: hidden;
    background: var(--card-white);
  }
  .card-art {
    position: absolute;
    inset: 0;
    width: 1080px;
    height: 714px;
  }
  .holder-name {
    position: absolute;
    left: 55px;
    top: 284px;
    max-width: 500px;
    margin: 0;
    font-family: "Syncopate", "Arial Black", sans-serif;
    font-size: 46px;
    line-height: 1;
    font-weight: 700;
    letter-spacing: 1px;
    color: var(--ink);
    white-space: nowrap;
  }
  .contact-list {
    position: absolute;
    left: 58px;
    top: 357px;
    margin: 0;
    padding: 0;
    list-style: none;
    font-family: "Oswald", "Arial Narrow", sans-serif;
    font-weight: 400;
    font-size: 34px;
    color: var(--ink);
  }
  .contact-item {
    display: flex;
    align-items: center;
    height: 54px;
  }
  .contact-icon {
    width: 34px;
    height: 34px;
    margin-right: 12px;
    flex: none;
  }
  .offer-list {
    position: absolute;
    right: 58px;
    top: 516px;
    margin: 0;
    padding: 0;
    list-style: none;
    font-family: "Archivo Narrow", "Arial Narrow", sans-serif;
    font-size: 23px;
    color: var(--text-light);
    text-align: right;
  }
  .offer-item {
    display: flex;
    justify-content: flex-end;
    align-items: center;
    height: 48px;
  }
  .offer-marker {
    width: 20px;
    height: 20px;
    margin-left: 12px;
    flex: none;
  }
</style>
</head>
<body>
  <section class="business-card">
    <svg class="card-art" viewBox="0 0 1080 714" xmlns="http://www.w3.org/2000/svg">
      <defs>
        <linearGradient id="slateFill" x1="0" y1="0" x2="0.6" y2="1">
          <stop offset="0" stop-color="var(--slate-mid)"/>
          <stop offset="1" stop-color="var(--slate-dark)"/>
        </linearGradient>
        <linearGradient id="screenFill" x1="0" y1="0" x2="1" y2="1">
          <stop offset="0" stop-color="var(--screen-mid)"/>
          <stop offset="1" stop-color="var(--screen-dark)"/>
        </linearGradient>
      </defs>
      <rect class="slate-field" width="1080" height="714" fill="url(#slateFill)"/>
      <path class="metal-band" fill="var(--slate-band)"
        d="M0,520 C80,552 200,570 380,548 C720,494 962,262 995,0 H943 C930,250 700,480 380,535 C200,560 80,545 0,520 Z"/>
      <path class="white-field" fill="var(--card-white)"
        d="M0,0 H943 C930,250 700,480 380,535 C200,560 80,545 0,520 Z"/>
      <g class="tv-photo" role="img" aria-label="Photo of two flat-screen televisions showing landscape and city-at-night scenes">
        <rect x="582" y="131" width="378" height="235" rx="4" fill="url(#screenFill)"/>
        <rect x="761" y="267" width="258" height="218" rx="4" fill="url(#screenFill)"/>
      </g>
    </svg>

    <h1 class="holder-name">GLEN MARSH</h1>

    <ul class="contact-list">
      <li class="contact-item">
        <svg class="contact-icon" viewBox="0 0 34 34" aria-hidden="true">
          <rect x="9" y="2" width="16" height="30" rx="3" fill="var(--icon-blue)"/>
          <rect x="12" y="6" width="10" height="19" fill="#ffffff"/>
          <circle cx="17" cy="28.5" r="1.6" fill="#ffffff"/>
        </svg>
        <span class="contact-phone">07841526094</span>
      </li>
      <li class="contact-item">
        <svg class="contact-icon" viewBox="0 0 34 34" aria-hidden="true">
          <rect x="2" y="8" width="30" height="20" fill="var(--icon-blue)"/>
          <path d="M3,9 L17,20 L31,9" fill="none" stroke="#ffffff" stroke-width="2"/>
          <path d="M3,27 L13,17 M31,27 L21,17" fill="none" stroke="#ffffff" stroke-width="1.5"/>
        </svg>
        <span class="contact-email">glmarsh@quinvale-mail.com</span>
      </li>
    </ul>

    <ul class="offer-list">
      <li class="offer-item">Selling Televisions, Velmora, Kira, Dravelux, Ronavi
        <svg class="offer-marker" viewBox="0 0 20 20" aria-hidden="true"><path d="M10,1 L13,5 H11 V9 H15 V7 L19,10 L15,13 V11 H11 V15 H13 L10,19 L7,15 H9 V11 H5 V13 L1,10 L5,7 V9 H9 V5 H7 Z" fill="#ffffff"/></svg>
      </li>
      <li class="offer-item">The latest models, sizes ranging from 22"- 75"
        <svg class="offer-marker" viewBox="0 0 20 20" aria-hidden="true"><path d="M10,1 L13,5 H11 V9 H15 V7 L19,10 L15,13 V11 H11 V15 H13 L10,19 L7,15 H9 V11 H5 V13 L1,10 L5,7 V9 H9 V5 H7 Z" fill="#ffffff"/></svg>
      </li>
      <li class="offer-item">Surround Sounds, Sound Bars and Wall Mounts
        <svg class="offer-marker" viewBox="0 0 20 20" aria-hidden="true"><path d="M10,1 L13,5 H11 V9 H15 V7 L19,10 L15,13 V11 H11 V15 H13 L10,19 L7,15 H9 V11 H5 V13 L1,10 L5,7 V9 H9 V5 H7 Z" fill="#ffffff"/></svg>
      </li>
    </ul>
  </section>
</body>
</html>
```